Business Card for Ferncliff Massage

I need a business card for my massage therapy & cannabis oil practice. I already have a logo,the "massage" got edited out of this file. I will send the original soon. I need these elements to be on the card:
web: FerncliffMassage.example
ph: 541/382-9147
email: Marla.Quintavelle@mailbox.example
Other slogans, statements to consider:
Science Geek, Massage Therapist, Neuromuscular Therapy, Cannabis Spa Treatments, Raindrop Therapy, Essential Oils
Target Market(s)
women between 20 & 65, people with enough $ to afford regular massage, people who recently had a motor vehicle accident, Halvora HMC insured
Industry/Entity Type
Massage Therapy
Contact Information for Business Card
I would like to see my bear logo featured; contact details, greens & blues preferred colors.

```html
<!DOCTYPE html>
<html lang="en">
<head>
<meta charset="utf-8">
<title>Ferncliff Massage – Business Card</title>
<link rel="stylesheet" href="https://fonts.googleapis.com/css2?family=Noto+Serif:wght@300;400;700&display=swap">
<style>
  :root {
    --backdrop: #9b9b9b;
    --card-white: #ffffff;
    --band-green: #3d8240;
    --brand-green: #4b8b4e;
    --stone-taupe: #a39388;
    --ink-light: #ffffff;
  }
  * { box-sizing: border-box; margin: 0; padding: 0; }
  html, body {
    width: 1200px;
    height: 1200px;
    overflow: hidden;
  }
  body {
    background: var(--backdrop);
    display: flex;
    align-items: center;
    justify-content: center;
    font-family: "Noto Serif", Georgia, serif;
  }
  .business-card {
    width: 1050px;
    height: 600px;
    background: var(--card-white);
    display: flex;
    flex-direction: column;
    box-shadow: 0 10px 30px rgba(0, 0, 0, 0.25);
  }
  .card-brand {
    height: 330px;
    display: flex;
    align-items: flex-end;
    padding: 0 0 40px 260px;
    gap: 22px;
  }
  .brand-dot {
    width: 64px;
    height: 64px;
    border-radius: 50%;
    background: var(--stone-taupe);
    margin-bottom: 10px;
  }
  .brand-name {
    font-weight: 300;
    font-size: 84px;
    line-height: 1;
    color: var(--brand-green);
    letter-spacing: 1px;
  }
  .card-contact {
    flex: 1;
    background: var(--band-green);
    color: var(--ink-light);
    padding: 34px 0 0 270px;
  }
  .contact-name {
    font-weight: 700;
    font-size: 36px;
    margin-bottom: 14px;
  }
  .contact-list {
    list-style: none;
    padding-left: 44px;
    font-weight: 400;
    font-size: 25px;
    line-height: 1.55;
  }
</style>
</head>
<body>
  <main class="business-card">
    <header class="card-brand">
      <span class="brand-dot" aria-hidden="true"></span>
      <span class="brand-name">Ferncliff</span>
    </header>
    <section class="card-contact">
      <h1 class="contact-name">Marla Quintavelle</h1>
      <ul class="contact-list">
        <li>541/382-9147</li>
        <li>FerncliffMassage.example</li>
        <li>Marla.Quintavelle@mailbox.example</li>
        <li>2276 NW Alder Crest Rd Bend, OR, 97703</li>
      </ul>
    </section>
  </main>
</body>
</html>
```